MARKETING MY MEDICAL PRACTICE

I am a physician providing medical-legal evaluations for competing attorneys (applicant attorneys representing injured workers versus defense attorneys and health insurance companies representing employers). Each opposing side wants me to be more biased toward their side. I am looking for a classy/elegant graphic design to apply to an exhibit booth LED backlit display, website, and printed brochures/business cards. I like the basic feel of the uploaded files IMG 1842 and IMG 1837. My medical practice focuses on evaluating patients with nerve, muscle, and skeletal injuries. I would like to include the three football players representing the nervous, muscular, and skeletal systems as well as the tools of my trade (goniometer measuring the knee range of motion, reflex hammer, and stethoscope with judge's gavel and hammer to describe what I do). I would like the goniometer, reflex hammer, and gavel & hammer to be faded into the back ground. The football players should be less opaque and more obvious.
I want my name in large big bold letters across the top of the graphics design: GORDON P. WEXLEY, M.D.
In smaller font below my name please place: Physical Medicine
One of the pics of me should be (with the backgrounds eliminated) on the side of my name (next to GORDON, not next to M.D.). I am not sure which pic would be better or more professionally appropriate.
On the other side of my name should be the illustration of the man showing muscular, skeletal, and nervous systems. It's my logo. I will supply the actual vector file of this logo once I receive it.
Somewhere in the graphics include: QME, AME, IME, & SIBTF evaluation
Somewhere in the graphics include: Physical Medicine: The specialty for neurological and musculoskeletal injuries in one evaluation by one doctor
Attorneys who refer injured workers for evaluation
MEDICAL SERVICES

```html
<!DOCTYPE html>
<html lang="en">
<head>
<meta charset="utf-8">
<title>Gordon P. Wexley, M.D. — Physical Medicine Display</title>
<link href="https://fonts.googleapis.com/css2?family=Bebas+Neue&family=Montserrat:wght@500;600;700;800&family=Oswald:wght@500&display=swap" rel="stylesheet">
<style>
  :root{
    --canvas:#e4e4e4;
    --paper:#ffffff;
    --ink:#141414;
    --crimson:#b93a3e;
    --gold:#d4b15e;
    --gold-soft:#e6d3a3;
    --night:#231f21;
    --skin:#b98d74;
  }
  *{box-sizing:border-box;margin:0;padding:0}
  html,body{width:800px;height:1200px;overflow:hidden}
  body{background:var(--canvas);position:relative;font-family:"Montserrat",sans-serif}
  .display{position:absolute;left:20px;top:297px;width:760px;height:606px;background:var(--paper);overflow:hidden;box-shadow:0 14px 40px rgba(0,0,0,.25)}
  .display__shade{position:absolute;left:0;top:0;width:344px;height:344px;background:linear-gradient(180deg,#f1f1f1,#f6f6f6)}
  .faded-tool{position:absolute;opacity:.6}
  .faded-tool--gavel{left:0;top:30px;width:170px;height:180px;background:radial-gradient(ellipse at 40% 50%,#cfcfcf,rgba(240,240,240,0) 70%)}
  .faded-tool--hammer{left:530px;top:200px;width:130px;height:110px;background:radial-gradient(ellipse at 50% 50%,#d6d6d6,rgba(245,245,245,0) 70%)}
  .faded-tool--goniometer{left:10px;top:240px;width:90px;height:90px;border-radius:50%;background:radial-gradient(circle,rgba(120,20,25,.35),rgba(185,58,62,0) 70%)}

  .name{position:absolute;left:0;right:0;top:14px;text-align:center;font-family:"Bebas Neue",sans-serif;font-weight:400;font-size:80px;line-height:1;color:var(--ink);letter-spacing:.3px}
  .specialty{position:absolute;left:0;right:0;top:95px;text-align:center;font-weight:700;font-size:27px;line-height:32px;color:var(--crimson);letter-spacing:1px}
  .rule{position:absolute;top:110px;height:2px;background:var(--gold)}
  .rule--left{left:84px;width:112px}
  .rule--right{left:564px;width:112px}
  .tagline{position:absolute;left:0;width:760px;text-align:center;color:var(--ink);line-height:20px}
  .tagline--lead{top:135px;font-weight:500;font-size:15px;letter-spacing:.5px}
  .tagline--focus{top:157px;font-weight:700;font-size:21px;line-height:24px;color:var(--crimson);letter-spacing:.8px}
  .tagline--close{top:184px;font-weight:500;font-size:15px;letter-spacing:.5px}
  .dots{position:absolute;left:362px;top:219px;display:flex;gap:2px}
  .dots span{width:9px;height:9px;border-radius:50%;background:var(--gold-soft)}
  .dots span:nth-child(n+3){background:var(--gold)}

  .service{position:absolute;display:flex;align-items:center;gap:15px;font-weight:800;font-size:35px;line-height:40px;color:var(--crimson);white-space:nowrap}
  .service svg{width:24px;height:24px;flex:none}
  .service--qme{left:224px;top:236px}
  .service--ame{left:224px;top:286px}
  .service--ime{left:412px;top:236px}
  .service--sibtf{left:412px;top:286px}
  .services__divider{position:absolute;left:384px;top:244px;height:76px;border-left:2px dotted #333}

  .logo-figure{position:absolute;left:658px;top:101px;width:85px;height:222px;border-radius:40px 40px 20px 20px;background:linear-gradient(90deg,#f0c04a 0%,#f1a46a 50%,#c9463f 100%)}

  .night-band{position:absolute;left:250px;top:344px;width:510px;height:239px;background:var(--night)}
  .crimson-panel{position:absolute;left:0;top:0;width:760px;height:606px}
  .gold-bar{position:absolute;left:276px;top:583px;width:484px;height:11px;background:var(--gold)}

  .player{position:absolute;top:366px;width:102px;height:206px;border-radius:46px 46px 28px 28px}
  .player--nerve{left:314px;background:linear-gradient(180deg,#2d56b8,#17306f);box-shadow:inset 0 0 24px rgba(230,190,90,.45)}
  .player--muscle{left:469px;background:linear-gradient(180deg,#2b4fb0,#8a2a3a 55%,#1b3476)}
  .player--bone{left:619px;background:linear-gradient(180deg,#3463d0,#183a8a)}
  .player-divider{position:absolute;top:370px;width:2px;height:190px;background:linear-gradient(180deg,rgba(60,110,220,0),#3a6ed8,rgba(60,110,220,0));transform:rotate(4deg)}

  .portrait{position:absolute;left:31px;top:214px;width:233px;height:392px}
  .portrait__head{position:absolute;left:80px;top:0;width:80px;height:124px;border-radius:40px 40px 36px 36px;background:linear-gradient(180deg,#3a2a24 0%,#3a2a24 18%,var(--skin) 30%,#a47b66 100%)}
  .portrait__body{position:absolute;left:0;top:120px;width:233px;height:272px;border-radius:40px 40px 0 0;background:linear-gradient(180deg,#252224,#1e1b1d)}

  .contact{position:absolute;left:34px;top:501px;width:238px;height:81px;border-radius:14px;background:var(--night);border:2px solid var(--crimson)}
  .contact__mark{position:absolute;left:13px;top:7px;width:24px;height:64px;border-radius:11px 11px 6px 6px;background:linear-gradient(90deg,#f0c04a,#c9463f)}
  .contact__label{position:absolute;left:45px;top:6px;font-family:"Oswald",sans-serif;font-weight:500;color:#fff;line-height:1;white-space:nowrap}
  .contact__label small{display:block;font-size:11px;line-height:13px}
  .contact__label strong{display:block;font-weight:500;font-size:16px;line-height:19px;letter-spacing:-.2px}
  .contact__rule{position:absolute;left:45px;top:43px;width:180px;height:1px;background:var(--crimson)}
  .contact__phone{position:absolute;left:45px;top:50px;display:flex;align-items:center;gap:8px;font-weight:700;font-size:17px;line-height:20px;color:var(--gold-soft);letter-spacing:1px;white-space:nowrap}
  .contact__phone svg{width:14px;height:14px}
</style>
</head>
<body>
  <main class="display">
    <div class="display__shade"></div>
    <div class="faded-tool faded-tool--gavel" role="img" aria-label="Faded judge's gavel and stethoscope in the background"></div>
    <div class="faded-tool faded-tool--hammer" role="img" aria-label="Faded reflex hammer in the background"></div>

    <h1 class="name">GORDON P. WEXLEY, M.D.</h1>
    <span class="rule rule--left"></span>
    <h2 class="specialty">PHYSICAL MEDICINE</h2>
    <span class="rule rule--right"></span>

    <p class="tagline tagline--lead">THE SPECIALTY FOR</p>
    <p class="tagline tagline--focus">NEUROLOGICAL &amp; MUSCULOSKELETAL</p>
    <p class="tagline tagline--close">INJURIES IN ONE EVALUATION BY ONE DOCTOR</p>

    <div class="dots"><span></span><span></span><span></span><span></span></div>

    <div class="service service--qme"><svg viewBox="0 0 26 26" fill="none" stroke="#222" stroke-width="2.4" stroke-linecap="round" stroke-linejoin="round"><path d="M20 13v8a2 2 0 0 1-2 2H5a2 2 0 0 1-2-2V8a2 2 0 0 1 2-2h9"/><path d="M8 13l4 4 11-11"/></svg>QME</div>
    <div class="service service--ame"><svg viewBox="0 0 26 26" fill="none" stroke="#222" stroke-width="2.4" stroke-linecap="round" stroke-linejoin="round"><path d="M20 13v8a2 2 0 0 1-2 2H5a2 2 0 0 1-2-2V8a2 2 0 0 1 2-2h9"/><path d="M8 13l4 4 11-11"/></svg>AME</div>
    <span class="services__divider"></span>
    <div class="service service--ime"><svg viewBox="0 0 26 26" fill="none" stroke="#222" stroke-width="2.4" stroke-linecap="round" stroke-linejoin="round"><path d="M20 13v8a2 2 0 0 1-2 2H5a2 2 0 0 1-2-2V8a2 2 0 0 1 2-2h9"/><path d="M8 13l4 4 11-11"/></svg>IME</div>
    <div class="service service--sibtf"><svg viewBox="0 0 26 26" fill="none" stroke="#222" stroke-width="2.4" stroke-linecap="round" stroke-linejoin="round"><path d="M20 13v8a2 2 0 0 1-2 2H5a2 2 0 0 1-2-2V8a2 2 0 0 1 2-2h9"/><path d="M8 13l4 4 11-11"/></svg>SIBTF</div>

    <div class="logo-figure" role="img" aria-label="Practice logo: anatomical figure showing muscular, skeletal and nervous systems"></div>

    <div class="night-band"></div>
    <svg class="crimson-panel" viewBox="0 0 760 606" aria-hidden="true">
      <polygon points="0,211 72,211 86,225 160,344 250,344 250,560 280,606 0,606" fill="#b93a3e"/>
      <polygon points="0,211 72,211 86,225 120,290 0,300" fill="#a83236" opacity=".6"/>
      <polyline points="0,199 70,199 82,211" fill="none" stroke="#d4b15e" stroke-width="2"/>
    </svg>
    <div class="faded-tool faded-tool--goniometer" role="img" aria-label="Faded goniometer in the background"></div>
    <div class="gold-bar"></div>

    <div class="player player--nerve" role="img" aria-label="X-ray football player showing the nervous system"></div>
    <span class="player-divider" style="left:430px"></span>
    <div class="player player--muscle" role="img" aria-label="X-ray football player showing the muscular system"></div>
    <span class="player-divider" style="left:599px"></span>
    <div class="player player--bone" role="img" aria-label="X-ray football player showing the skeletal system"></div>

    <div class="portrait" role="img" aria-label="Portrait photo of the doctor in black scrubs, arms crossed">
      <div class="portrait__head"></div>
      <div class="portrait__body"></div>
    </div>

    <div class="contact">
      <div class="contact__mark" role="img" aria-label="Small practice logo figure"></div>
      <p class="contact__label"><small>OFFICES -</small><strong>THROUGHOUT CALIFORNIA</strong></p>
      <span class="contact__rule"></span>
      <p class="contact__phone">
        <svg viewBox="0 0 24 24" fill="#fff"><path d="M6.6 10.8a15 15 0 0 0 6.6 6.6l2.2-2.2a1 1 0 0 1 1-.25 11.4 11.4 0 0 0 3.6.57 1 1 0 0 1 1 1V20a1 1 0 0 1-1 1A17 17 0 0 1 3 4a1 1 0 0 1 1-1h3.5a1 1 0 0 1 1 1c0 1.25.2 2.45.57 3.57a1 1 0 0 1-.25 1z"/></svg>
        555-014-2287</p>
    </div>
  </main>
</body>
</html>
```